Property refurbishment & maintenance Business Card Design

Velmorin Ltd is a leading provider of domestic maintenance, building and refurbishment services. Founded in October 2009 by Piotr Velmorin, we aim to provide our customers with exceptional home improvement and maintenance services whilst minimising the disruption and stress caused.
The building services we provide are of the very highest quality. We provide all of your customers with the peace of mind in knowing that they are dealing with experts in construction, renovation and decoration. This is because we are members of the Guild of Craft Contractors (GCC). We have also had our credentials verified by Surelink and the UK government's Keel Seal scheme.
Target Market(s)
Private home owners,letting agents,tenants
Industry/Entity Type
Home Improvement
Contact Information for Business Card
Velmorin ltd.
Piotr Velmorin
14 Pellham Birch Lane ,Waltham Cross,Herts,EN7 2QR,T.01707318257 M:07924168330
E. info@velmorin.example. www.velmorin.example
Look and feel
Each slider illustrates characteristics of the customer's brand and the style your logo design should communicate.

```html
<!DOCTYPE html>
<html lang="en">
<head>
<meta charset="utf-8">
<title>Velmorin Ltd — Business Card</title>
<link rel="stylesheet" href="https://fonts.googleapis.com/css2?family=Arimo:wght@400&display=swap">
<style>
  :root {
    --page: #ffffff;
    --trim: #d8262b;
    --card-edge: #000000;
    --card-glow: #3a2218;
    --gold: #d4a27a;
    --mark: #c79c6c;
    --copper: #d38c5a;
    --rule: #d08a58;
  }
  * { margin: 0; padding: 0; box-sizing: border-box; }
  html, body {
    width: 1200px;
    height: 995px;
    overflow: hidden;
    background: var(--page);
    font-family: "Arimo", Arial, sans-serif;
  }
  .sheet { position: relative; width: 1200px; height: 995px; }
  .card-frame {
    position: absolute;
    left: 260px;
    width: 705px;
    height: 456px;
    border: 2px solid var(--trim);
  }
  .card-frame--front { top: 17px; }
  .card-frame--back { top: 507px; }
  .card {
    position: absolute;
    left: 12px;
    top: 12px;
    width: 677px;
    height: 428px;
    background: radial-gradient(ellipse 55% 60% at 45% 52%, var(--card-glow) 0%, #1a0f0b 55%, var(--card-edge) 100%);
  }
  .card svg { display: block; width: 677px; height: 428px; }
  .brand-mark { fill: var(--mark); opacity: 0.9; }
  .brand-name { fill: var(--gold); font-size: 44px; }
  .tagline { fill: var(--gold); font-size: 20.5px; }
  .person-name { fill: var(--copper); font-size: 40px; }
  .detail { fill: var(--copper); font-size: 22px; }
  .divider { stroke: var(--rule); stroke-width: 5; stroke-linecap: round; }
</style>
</head>
<body>
<main class="sheet">
  <section class="card-frame card-frame--front" aria-label="Card front">
    <div class="card">
      <svg viewBox="0 0 677 428" xmlns="http://www.w3.org/2000/svg">
        <rect class="brand-mark" x="250" y="50" width="240" height="240" role="img" aria-label="Velmorin Ltd brand mark"/>
        <text class="brand-name" x="253" y="331">Velmorin Ltd</text>
        <text class="tagline" x="339" y="376" text-anchor="middle" textLength="572" lengthAdjust="spacing">Domestic Maintenance, Building and Refurbishment Services</text>
      </svg>
    </div>
  </section>

  <section class="card-frame card-frame--back" aria-label="Card back">
    <div class="card">
      <svg viewBox="0 0 677 428" xmlns="http://www.w3.org/2000/svg">
        <text class="person-name" x="28" y="176">Piotr Velmorin</text>
        <text class="detail" x="28" y="215">14 Pellham Birch Lane</text>
        <text class="detail" x="28" y="245">Waltham Cross Hertz</text>
        <text class="detail" x="28" y="275">EN7 2QR</text>

        <line class="divider" x1="351" y1="73" x2="351" y2="352"/>

        <text class="detail" x="372" y="216">t:<tspan x="404">01707318257</tspan></text>
        <text class="detail" x="372" y="246">m:<tspan x="404">07924168330</tspan></text>
        <text class="detail" x="372" y="276">e:<tspan x="404">info@velmorin.example</tspan></text>
        <text class="detail" x="372" y="306">w:<tspan x="408">www.velmorin.example</tspan></text>
      </svg>
    </div>
  </section>
</main>
</body>
</html>
```